Business card for Internet Marketing Consultant

Simple - need a nice business card design using the logo elements and colors. Keywords: Progressive, professional, stylish, minimalist. Please use the kr as part of the design.

Info for card:

Gareth Pennock
Internet Marketing Strategist
Phone: (555) 813-2064
Email: gareth@korvantareach.com
Address: 2156 N. Halvern Ave., Ste. 118
Brenton Vale, Arizona 85990

Website: www.korvantareach.com

Business

Sans Serif

```html
<!DOCTYPE html>
<html lang="en">
<head>
<meta charset="utf-8">
<title>Korvanta Reach – Business Card</title>
<link rel="stylesheet" href="https://fonts.googleapis.com/css2?family=Montserrat:wght@600;700&family=Questrial&display=swap">
<style>
  :root {
    --stage: #343941;
    --card-white: #ffffff;
    --brand-green: #7cc87d;
    --brand-green-line: #6bb06c;
    --brand-blue: #1478d4;
    --ink: #3b3d40;
    --ink-soft: #55585c;
  }
  * { box-sizing: border-box; margin: 0; padding: 0; }
  html, body {
    width: 1200px;
    height: 960px;
    overflow: hidden;
    background: var(--stage);
  }
  .stage {
    width: 1200px;
    height: 960px;
    display: flex;
    align-items: center;
    justify-content: center;
    gap: 48px;
  }
  .card {
    position: relative;
    width: 520px;
    height: 297px;
    overflow: hidden;
    box-shadow: 0 10px 28px rgba(0, 0, 0, 0.35);
  }

  /* Contact side */
  .card--contact { background: var(--card-white); }
  .card--contact .decor-ring {
    position: absolute;
    right: -40px;
    top: 18px;
    width: 240px;
    height: 240px;
  }
  .contact {
    position: absolute;
    left: 40px;
    top: 62px;
    font-family: "Questrial", "Century Gothic", sans-serif;
    color: var(--ink);
    font-size: 14px;
    line-height: 1.3;
  }
  .contact__name {
    font-family: "Montserrat", sans-serif;
    font-weight: 700;
    font-size: 19px;
    letter-spacing: 0.02em;
    text-transform: uppercase;
    color: var(--brand-blue);
    line-height: 1.1;
  }
  .contact__title { color: var(--ink-soft); margin-bottom: 20px; }
  .contact__lines { list-style: none; margin-bottom: 20px; }
  .contact__label {
    display: inline-block;
    width: 16px;
    color: var(--brand-blue);
  }
  .contact__address { font-style: normal; margin-bottom: 22px; }
  .contact__web {
    font-family: "Montserrat", sans-serif;
    font-weight: 600;
    font-size: 14px;
    color: var(--brand-blue);
  }

  /* Brand side */
  .card--brand { background: var(--brand-green); }
  .card--brand .decor-ring {
    position: absolute;
    right: 30px;
    top: 50px;
    width: 190px;
    height: 190px;
  }
  .brand-lockup {
    position: absolute;
    left: 56px;
    top: 108px;
    display: flex;
    align-items: center;
    gap: 14px;
  }
  .brand-lockup__dot {
    width: 58px;
    height: 58px;
    border-radius: 50%;
    background: var(--brand-blue);
    flex: none;
  }
  .brand-lockup__name {
    font-family: "Montserrat", sans-serif;
    font-weight: 700;
    font-size: 38px;
    line-height: 1;
    color: var(--card-white);
    letter-spacing: -0.01em;
  }
  .brand-lockup__tagline {
    margin-top: 8px;
    font-family: "Questrial", "Century Gothic", sans-serif;
    font-size: 13px;
    letter-spacing: 0.24em;
    color: var(--card-white);
  }
</style>
</head>
<body>
  <main class="stage">
    <section class="card card--contact" aria-label="Business card, contact side">
      <svg class="decor-ring" viewBox="0 0 240 240" aria-hidden="true">
        <circle cx="120" cy="120" r="100" fill="none" stroke="var(--brand-blue)" stroke-width="1.6"/>
      </svg>
      <div class="contact">
        <h1 class="contact__name">Gareth Pennock</h1>
        <p class="contact__title">Internet Marketing Strategist</p>
        <ul class="contact__lines">
          <li><span class="contact__label">T</span>(555) 813-2064</li>
          <li><span class="contact__label">E</span>gareth@korvantareach.com</li>
        </ul>
        <address class="contact__address">
          2156 N. Halvern Ave., Ste. 118<br>
          Brenton Vale, Arizona 85990
        </address>
        <p class="contact__web">www.korvantareach.com</p>
      </div>
    </section>

    <section class="card card--brand" aria-label="Business card, brand side">
      <svg class="decor-ring" viewBox="0 0 190 190" aria-hidden="true">
        <circle cx="95" cy="95" r="80" fill="none" stroke="var(--brand-green-line)" stroke-width="1.6"/>
      </svg>
      <div class="brand-lockup">
        <span class="brand-lockup__dot" aria-hidden="true"></span>
        <div>
          <p class="brand-lockup__name">korvantareach</p>
          <p class="brand-lockup__tagline">INTERNET MARKETING STRATEGIES</p>
        </div>
      </div>
    </section>
  </main>
</body>
</html>
```